Business Card Re-Design for a Lighting Designer

I would like my business card re-designed. It is currently high gloss and they scratch too easily. I don not think the current design lends itself well to a matte finish. I have included the current design for reference along with our company logo.
Check out our website for current branding.
http://www.brambleorchidstudio.example

Updates
Some of the top contenders are muslim and it is a holiday for them. I do not want to discriminate and would expect the same courtesy for holidays we celebrate.
Target Market(s)
Interior Designers, Architects
Contact Information for Business Card
Logo - Name, Title, Address, Telephone Number and Extension, Email
Font styles to use
Requirements
Must have
- All the information listed on the current business card. If you use Red, it needs to be the red from our logo.
Nice to have
- Vertical and Horizontal Designs will be entertained.
Should not have
- Requirements for a glossy finish...should not look too corporate since we are a design firm.

```html
<!DOCTYPE html>
<html lang="en">
<head>
<meta charset="utf-8">
<title>Bramble Orchid Studio — Business Card</title>
<link rel="stylesheet" href="https://fonts.googleapis.com/css2?family=Poppins:wght@300;400;600&display=swap">
<style>
  :root {
    --brand-red: #990000;
    --band-black: #121212;
    --bar-grey: #9a9a9a;
    --text-grey: #555555;
    --card-white: #ffffff;
    --page-bg: #ececec;
  }
  * { margin: 0; padding: 0; box-sizing: border-box; }
  html, body { width: 1125px; height: 1200px; overflow: hidden; }
  body {
    background: var(--page-bg);
    font-family: "Poppins", Arial, sans-serif;
    position: relative;
  }
  .card {
    position: absolute;
    left: 162px;
    width: 800px;
    height: 457px;
    overflow: hidden;
  }
  .card-front { top: 100px; background: var(--card-white); }
  .card-back { top: 630px; background: var(--brand-red); }

  /* front */
  .name-band {
    position: absolute; left: 0; top: 175px;
    width: 510px; height: 70px;
    background: var(--band-black);
    display: flex; align-items: center;
    padding-left: 45px; gap: 14px;
  }
  .person-name {
    color: var(--brand-red); font-weight: 600; font-size: 25px; letter-spacing: 0.3px;
  }
  .person-title { color: #fff; font-weight: 400; font-size: 20px; }
  .accent-bar {
    position: absolute; left: 0; top: 257px;
    width: 510px; height: 18px; background: var(--bar-grey);
  }
  .brand-square {
    position: absolute; left: 722px; top: 62px;
    width: 78px; height: 126px; background: var(--brand-red);
  }
  .brand-name {
    position: absolute; left: 516px; top: 150px;
    color: var(--band-black); font-weight: 400;
    font-size: 34px; line-height: 40px;
  }
  .contact-list, .address {
    position: absolute; list-style: none;
    color: var(--text-grey); font-size: 17px; line-height: 21.5px;
  }
  .contact-list { left: 50px; top: 340px; }
  .contact-list li { display: flex; align-items: center; gap: 8px; }
  .icon { width: 15px; height: 15px; fill: var(--brand-red); flex: none; }
  .address { left: 494px; top: 344px; display: flex; gap: 6px; align-items: flex-start; }
  .address .icon { margin-top: 3px; }

  /* back */
  .back-name {
    position: absolute; left: 0; right: 0; top: 180px;
    text-align: center; color: #fff;
    font-weight: 400; font-size: 52px; line-height: 60px;
  }
  .back-url {
    position: absolute; left: 0; right: 0; top: 394px;
    text-align: center; color: #fff;
    font-weight: 400; font-size: 18px; letter-spacing: 5px;
  }
</style>
</head>
<body>
  <section class="card card-front">
    <div class="name-band">
      <span class="person-name">MARIAN SOLACE</span>
      <span class="person-title">Principal</span>
    </div>
    <div class="accent-bar"></div>
    <div class="brand-square"></div>
    <div class="brand-name">BRAMBLE<br>ORCHID<br>STUDIO</div>

    <ul class="contact-list">
      <li>
        <svg class="icon" viewBox="0 0 16 16"><path d="M3.6 1.2l2.3 2.5-1.3 2a9 9 0 0 0 5.7 5.7l2-1.3 2.5 2.3-1.4 2.2C7.6 15 1 8.4 1.4 2.6z"/></svg>
        <span>555.010.2470x1</span>
      </li>
      <li>
        <svg class="icon" viewBox="0 0 16 16"><path d="M1 3.5h14v9H1z M1.5 4l6.5 5 6.5-5" stroke="#fff" stroke-width="1"/></svg>
        <span>marian@brambleorchidstudio.example</span>
      </li>
      <li>
        <svg class="icon" viewBox="0 0 16 16"><circle cx="8" cy="8" r="7"/><path d="M5 4c2 1 1 3 3 3s1 3-1 4M10 3c0 2 2 2 3 3" stroke="#fff" stroke-width="1.2" fill="none"/></svg>
        <span>brambleorchidstudio.example</span>
      </li>
    </ul>

    <div class="address">
      <svg class="icon" viewBox="0 0 16 16"><path d="M8 0.5a5.5 5.5 0 0 1 5.5 5.5C13.5 10 8 15.5 8 15.5S2.5 10 2.5 6A5.5 5.5 0 0 1 8 0.5z"/><circle cx="8" cy="6" r="2" fill="#fff"/></svg>
      <span>212 Fernwood row<br>Suite40 Lakeview<br>Georgia 30999 USA</span>
    </div>
  </section>

  <section class="card card-back">
    <div class="back-name">BRAMBLE<br>ORCHID STUDIO</div>
    <div class="back-url">WWW.BRAMBLEORCHIDSTUDIO.EXAMPLE</div>
  </section>
</body>
</html>
```